Flyer-Design für Amerikanische Chiropraktik
Zielgruppe
Praxis für Amerikanische Chiropraktik
Zielgruppe: Gesundheitsbewusste Menschen, gerne gebildet, Affinität zu Sport/Yoga etc.
Flyer soll modern und hochwertig sein (Zielgruppe auch Privatversicherte und Büroleute)
Aufgabenstellung
Bitte keine Schnörkel.
Klare Linien. Straight einfach
Positive Vibes
Website ist nicht final fertig. Das blau/grau und das Grün wird aber aller Voraussicht nach Weiter verwendet. Falls das rot verwendet wird eher nicht so oft bitte.
Sehr gerne für die Überschriften die gleichen Balken unter den Überschriften für den Flyer verwenden.
Flyer bei Nordra Druck ist 99x210 mm (ich denke mit etwas Spiel am Rand für den Druck.) 6 Seiten.
Auf der letzten Seite (sollte die mittlere Rückseite sein) bitte Kontaktdaten und evtl Portraitbild.

```html
<!DOCTYPE html>
<html lang="de">
<head>
<meta charset="utf-8">
<title>Flyer Chiropraktik Kasimir Holt</title>
<link href="https://fonts.googleapis.com/css2?family=Fira+Sans:wght@400;600;700&family=Poppins:ital,wght@0,300;0,500;0,600;0,700;1,700&display=swap" rel="stylesheet">
<style>
:root{
  --bg:#efefef;
  --dark:#2b2a2c;
  --dark-soft:#3a393c;
  --gold:#b8a67c;
  --gold-deep:#a8956a;
  --white:#ffffff;
  --ink:#232224;
  --ink-light:#e9e7e3;
}
*{margin:0;padding:0;box-sizing:border-box}
html,body{width:857px;height:1200px;overflow:hidden;background:var(--bg)}
body{position:relative;font-family:"Fira Sans",sans-serif}
.sheet{position:absolute;left:53px;width:751px;height:530px;overflow:hidden}
.sheet--outside{top:47px;background:var(--dark)}
.sheet--inside{top:618px;background:var(--white)}
.abs{position:absolute}
.shapes{position:absolute;left:0;top:0}
.heading{font-family:"Poppins",sans-serif;font-weight:600;font-size:11px;line-height:14px;white-space:nowrap}
.heading .accent{color:var(--gold)}
.heading--light{color:var(--white)}
.heading--dark{color:var(--ink)}
.bar{position:absolute;width:53px;height:2px;background:var(--gold)}
.copy{font-size:8.4px;line-height:13.35px;white-space:nowrap}
.copy--light{color:var(--ink-light)}
.copy--dark{color:var(--ink)}
.copy b{color:var(--gold);font-weight:600}
.symptoms{list-style:none;font-size:9.4px;line-height:13.35px;color:var(--ink-light)}
.symptoms li{position:relative;padding-left:13px;white-space:nowrap}
.symptoms li::before{content:"";position:absolute;left:3px;top:5px;width:4.5px;height:4.5px;border-radius:50%;background:var(--ink-light)}
.benefits{list-style:none}
.benefit{position:absolute;left:30px;width:220px}
.benefit svg{position:absolute;left:-1px;top:-4px}
.benefit p{margin-left:20px;font-size:8.6px;line-height:13.3px;color:var(--ink-light);white-space:nowrap}
.contact{position:absolute;left:250px;width:250px;text-align:center;color:var(--ink-light);font-size:8.5px;line-height:13px}
.contact .name{color:var(--gold);font-weight:600;font-size:10.5px}
.contact .web{color:var(--gold);font-weight:600;font-size:8.6px}
.welcome{position:absolute;left:268px;top:433px;width:110px;text-align:center;font-weight:700;font-size:12.5px;line-height:14px;color:var(--gold);transform:rotate(-5deg)}
.brand{position:absolute;left:500px;top:58px;width:251px;text-align:center;font-family:"Poppins",sans-serif;font-weight:500;font-size:10px;line-height:12px;letter-spacing:1.6px;color:var(--dark);text-transform:uppercase}
.title{position:absolute;left:500px;width:251px;text-align:center;color:var(--white);font-family:"Poppins",sans-serif}
.title--light{top:435px;font-weight:300;font-size:21.5px;line-height:26px}
.title--bold{top:462px;font-weight:700;font-size:21.5px;line-height:26px}
.claim{position:absolute;left:500px;top:493px;width:251px;text-align:center;font-family:"Poppins",sans-serif;font-weight:600;font-size:10.2px;color:var(--gold)}
.photo{position:absolute}
.cause-icon{position:absolute;left:270px;width:38px;height:36px;background:var(--dark-soft);border-radius:3px}
.cause{position:absolute;left:325px}
.cause h4{font-size:10px;line-height:13px;font-weight:600;color:var(--gold)}
.cause p{font-size:8.6px;line-height:13.35px;color:var(--ink-light);white-space:nowrap}
.footer-band{position:absolute;left:0;top:497px;width:751px;height:33px;background:var(--gold)}
.footer-band span{position:absolute;top:9px;font-family:"Poppins",sans-serif;font-style:italic;font-weight:700;font-size:11.5px;line-height:14px;color:var(--white);white-space:nowrap;transform:translateX(-50%)}
.footer-line{position:absolute;top:16px;height:2px;background:var(--white)}
</style>
</head>
<body>

<!-- Outside spread -->
<section class="sheet sheet--outside">
  <svg class="shapes" width="751" height="530" viewBox="0 0 751 530">
    <polygon points="0,0 250,0 250,143 121,170 0,143" fill="#b8a67c"/>
    <polygon points="500,0 751,0 751,383 630,418 500,391" fill="#b8a67c"/>
  </svg>

  <!-- Panel: Für wen -->
  <svg class="photo" style="left:0;top:0" width="250" height="165" viewBox="0 0 250 165" role="img" aria-label="Foto: Behandlungsliege mit Chiropraktik-Instrument">
    <defs><linearGradient id="gLiege" x1="0" y1="0" x2="0" y2="1"><stop offset="0" stop-color="#e4e0dc"/><stop offset="0.55" stop-color="#8b8a8c"/><stop offset="1" stop-color="#b98b5a"/></linearGradient></defs>
    <polygon points="0,0 250,0 250,136 121,162 0,136" fill="url(#gLiege)"/>
  </svg>

  <h2 class="heading heading--light abs" style="left:14px;top:182px">Für wen?</h2>
  <span class="bar" style="left:14px;top:203px"></span>
  <p class="copy copy--light abs" style="left:14px;top:259px;top:259px;top:259px;top:259px;top:259px;top:259px;top:259px;top:259px;top:259px;top:259px;top:259px;top:259px;top:259px;top:259px;top:259px;top:211px">
    Die Amerikanische Chiropraktik verfolgt einen<br>
    ganzheitlichen und ursachenbezogenen Ansatz,<br>
    wodurch sich vielseitige Anwendungsbereiche<br>
    ergeben. Unser Angebot reicht von Gesundheitsvor-<br>
    sorge bis hin zur Behandlung von bereits existieren-<br>
    den Störungen und Symptomen.Anwendungsgebiete
  </p>
  <h3 class="heading heading--light abs" style="left:16px;top:309px;font-size:11.5px">Daher besuchen uns Menschen mit:</h3>
  <span class="bar" style="left:16px;top:330px"></span>
  <ul class="symptoms abs" style="left:16px;top:338px">
    <li>Chronischer Stress</li>
    <li>Schwindel</li>
    <li>Müdigkeit</li>
    <li>Kopfschmerzen</li>
    <li>Migräne</li>
    <li>Schulter- und Armschmerzen</li>
    <li>Impingement-Syndrom</li>
    <li>Karpaltunnelsyndrom</li>
    <li>Beckenschiefstand</li>
    <li>Tinnitus</li>
    <li>Rückenschmerzen</li>
    <li>Bandscheibenvorfall</li>
    <li>Kribbeln und Taubheit in Händen oder Füßen</li>
  </ul>

  <!-- Panel: Kontakt -->
  <ul class="benefits">
    <li class="benefit" style="left:270px;top:20px">
      <svg width="20" height="20" viewBox="0 0 20 20"><circle cx="9" cy="10" r="7.5" fill="none" stroke="#b8a67c" stroke-width="1.8"/><path d="M5 10 l3.5 3.5 L18 3" fill="none" stroke="#b8a67c" stroke-width="2" stroke-linecap="round" stroke-linejoin="round"/></svg>
      <p>Wir sind Experten auf unserem Gebiet.</p>
    </li>
    <li class="benefit" style="left:270px;top:46px">
      <svg width="20" height="20" viewBox="0 0 20 20"><circle cx="9" cy="10" r="7.5" fill="none" stroke="#b8a67c" stroke-width="1.8"/><path d="M5 10 l3.5 3.5 L18 3" fill="none" stroke="#b8a67c" stroke-width="2" stroke-linecap="round" stroke-linejoin="round"/></svg>
      <p>Arbeiten nach neuesten Wissenschaftlichen<br>Kenntnissen.<br>Sanfte und zielgerichtete Behandlung.</p>
    </li>
    <li class="benefit" style="left:270px;top:100px">
      <svg width="20" height="20" viewBox="0 0 20 20"><circle cx="9" cy="10" r="7.5" fill="none" stroke="#b8a67c" stroke-width="1.8"/><path d="M5 10 l3.5 3.5 L18 3" fill="none" stroke="#b8a67c" stroke-width="2" stroke-linecap="round" stroke-linejoin="round"/></svg>
      <p>Profitieren Sie von langjährige praktische<br>Erfahrung und modernen neurowissenschaftli-<br>che Aspekten in der chiropraktischen Behand-<br>lung.</p>
    </li>
    <li class="benefit" style="left:270px;top:167px">
      <svg width="20" height="20" viewBox="0 0 20 20"><circle cx="9" cy="10" r="7.5" fill="none" stroke="#b8a67c" stroke-width="1.8"/><path d="M5 10 l3.5 3.5 L18 3" fill="none" stroke="#b8a67c" stroke-width="2" stroke-linecap="round" stroke-linejoin="round"/></svg>
      <p>Wir sind mit Freude und Engagement für Dich<br>und Deine Gesundheit da.</p>
    </li>
  </ul>
  <span class="abs" style="left:270px;top:208px;width:218px;height:2px;background:var(--gold)"></span>

  <address class="contact" style="top:227px;font-style:normal">
    <div class="name">Kasimir Holt</div>
    <div style="margin-top:3px">Heil- und Chiropraktiker,<br>B.Sc. Physiotherapie</div>
    <div style="margin-top:8px;line-height:15.5px">Ahornweg 6 | 83629 Weyarn<br>Tel: 0151/40528816<br>praxis@chiropraktik-holt.de</div>
    <div class="web" style="margin-top:4px">www.chiropraktik-holt.de</div>
  </address>

  <p class="welcome">Wir freuen uns<br>auf Dich!</p>
  <svg class="photo" style="left:382px;top:362px" width="112" height="168" viewBox="0 0 112 168" role="img" aria-label="Porträtfoto des Chiropraktikers im weißen T-Shirt">
    <defs><linearGradient id="gPortrait" x1="0" y1="0" x2="0" y2="1"><stop offset="0" stop-color="#6b5a4c"/><stop offset="0.35" stop-color="#c9a892"/><stop offset="0.7" stop-color="#f2f1ef"/><stop offset="1" stop-color="#aebccb"/></linearGradient></defs>
    <rect x="0" y="0" width="112" height="168" rx="40" fill="url(#gPortrait)"/>
  </svg>

  <!-- Panel: Titel -->
  <svg class="abs" style="left:617px;top:17px" width="36" height="36" viewBox="0 0 36 36"><circle cx="18" cy="18" r="16" fill="none" stroke="#2b2a2c" stroke-width="1.5"/></svg>
  <div class="brand">Chiropraktik<br>Kasimir Holt</div>
  <svg class="photo" style="left:527px;top:106px" width="224" height="312" viewBox="0 0 224 312" role="img" aria-label="Foto: Chiropraktiker umarmt eine Patientin">
    <defs><linearGradient id="gHug" x1="0" y1="0" x2="1" y2="1"><stop offset="0" stop-color="#c4ad86"/><stop offset="0.45" stop-color="#e2c7ad"/><stop offset="0.75" stop-color="#efe9e6"/><stop offset="1" stop-color="#d7c0c4"/></linearGradient></defs>
    <polygon points="0,0 224,0 224,271 103,306 0,285" fill="url(#gHug)"/>
  </svg>
  <svg class="shapes" width="751" height="530" viewBox="0 0 751 530">
    <polygon points="500,389 630,418 751,383 751,530 500,530" fill="#2b2a2c"/>
  </svg>
  <h1 class="title title--light">Dein Weg zu mehr</h1>
  <p class="title title--bold">Wohlbefinden</p>
  <p class="claim">MODERN. URSÄCHLICH. ANDERS</p>
</section>

<!-- Inside spread -->
<section class="sheet sheet--inside">
  <!-- Panel: Was ist Chiropraktik -->
  <h2 class="heading heading--dark abs" style="left:14px;top:13px">Was ist <span class="accent">Amerikanische Chiropraktik?</span></h2>
  <span class="bar" style="left:14px;top:35px"></span>
  <p class="copy copy--dark abs" style="left:14px;top:42px">
    Amerikanische Chiropraktik ist eine eigenständige,<br>
    ganzheitliche und vitalistische Form der Gesundheitsp-<br>
    flege, die darauf ausgerichtet ist, Gesundheit und<br>
    Funktion des menschlichen Körpers wiederherzustel-<br>
    len und zu erhalten.
  </p>
  <p class="copy copy--dark abs" style="left:14px;top:122px">
    Sie ist sowohl eine evidenzbasierte Wissenschaft als<br>
    auch eine Heilkunst und eine Philosophie, die nach<br>
    der optimalen Funktion des Nervensystems strebt.
  </p>
  <h3 class="heading heading--dark abs" style="left:14px;top:178px">Wie funktioniert <span class="accent">Chiropraktik?</span></h3>
  <span class="bar" style="left:14px;top:199px"></span>
  <p class="copy copy--dark abs" style="left:14px;top:207px">
    Der Körper wird von seinem Nervensystem gesteuert.<br>
    Es ist dafür verantwortlich, wie ein Mensch seine<br>
    Umwelt wahrnimmt und durch das Leben geht. Über<br>
    das Nervensystem empfängt und sendet das Gehirn<br>
    fortwährend Informationen an Organe, Muskeln und<br>
    alle anderen Strukturen. Seine optimale Funktion ist<br>
    demnach von größter Bedeutung.
  </p>
  <p class="copy copy--dark abs" style="left:14px;top:313px">
    Im besten Fall werden Körper und Psyche über das<br>
    Nervensystem in Balance gehalten. Dazu muss alles<br>
    störungsfrei miteinander vernetzt sein. Fehlstellungen<br>
    und Blockaden können die Vernetzung stören: Es<br>
    kommt zu sogenannten Subluxationen. Das physische<br>
    und psychische Gleichgewicht gerät ins Wanken.<br>
    Die Folgen können sehr vielfältig sein. Muskelverspan-<br>
    nungen, Nackenschmerzen, Kopfschmerzen oder<br>
    Rückenschmerzen können die Folge sein. Oft bleiben<br>
    solche <b>Subluxationen</b> über Jahre unbemerkt, bevor sie<br>
    Schmerzen und/oder psycho-emotionale Symptome<br>
    verursachen.
  </p>

  <!-- Panel: Subluxation -->
  <svg class="photo" style="left:250px;top:0" width="250" height="119" viewBox="0 0 250 119" role="img" aria-label="Foto: Hände des Chiropraktikers am Rücken einer Patientin">
    <defs><linearGradient id="gBack" x1="0" y1="0" x2="1" y2="0"><stop offset="0" stop-color="#cfcac6"/><stop offset="0.5" stop-color="#f4f2f0"/><stop offset="1" stop-color="#e2dbd3"/></linearGradient></defs>
    <rect width="250" height="114" fill="url(#gBack)"/>
    <rect y="114" width="250" height="5" fill="#b8a67c"/>
  </svg>
  <div class="abs" style="left:250px;top:119px;width:250px;height:378px;background:var(--dark)"></div>
  <h2 class="heading heading--light abs" style="left:270px;top:137px">Was ist eigentlich eine <span class="accent">Subluxation?</span></h2>
  <span class="bar" style="left:270px;top:158px"></span>
  <p class="copy copy--light abs" style="left:270px;top:165px">
    Wir definieren eine vertebrale Subluxation als ein<br>
    dysfunktionales Gebiet in der Wirbelsäule, dass sich<br>
    aufgrund seines Einflusses auf das Nervensystem<br>
    negativ auf die Gesundheit und das Wohlbefinden<br>
    auswirkt. Die Funktion der Wirbelsäule als wichtiger<br>
    Informationsgeber für das Gehirn ist gestört.
  </p>
  <h3 class="heading heading--light abs" style="left:270px;top:263px">Ursachen für eine <span class="accent">Subluxation</span></h3>

  <span class="cause-icon" style="top:304px" role="img" aria-label="Symbol: gestresste Person"></span>
  <div class="cause" style="top:296px"><h4>Physischer Stress</h4><p>wie z.B. Trauma (Brüche etc.) Unfälle,<br>langes Sitzen, Bewegungsmangel</p></div>
  <span class="cause-icon" style="top:363px" role="img" aria-label="Symbol: Viren und Giftstoffe"></span>
  <div class="cause" style="top:355px"><h4>Toxischer Stress</h4><p>wie z.B. Zigaretten, Alkohol, Drogen,<br>Abgase, Medikamente, Übersäuerung</p></div>
  <span class="cause-icon" style="top:417px" role="img" aria-label="Symbol: verspannter Rücken"></span>
  <div class="cause" style="top:411px"><h4>Psychischer Stress</h4><p>Macht einen großen Anteil aus. Druck<br>und hohe Anforderungen im Beruf,<br>Alltagsstress, Schlafmangel, Sorgen,<br>Überforderung.</p></div>

  <!-- Panel: Justierung -->
  <h2 class="heading heading--dark abs" style="left:514px;top:13px">Wie helfen wir? <span class="accent">Die Justierung</span></h2>
  <span class="bar" style="left:514px;top:35px"></span>
  <p class="copy copy--dark abs" style="left:514px;top:42px">
    Die chiropraktische Justierung korrigiert eine<br>
    <b>Subluxation</b>, indem sie das schadhafte neurologische<br>
    Muster durchbricht. Durch einen sanften und<br>
    gezielten Impuls wird die physiologische Beweglich-<br>
    keit und Position eines Gelenkes wieder hergestellt<br>
    und faszialer Adhäsionen gelöst. Die Impulse führen<br>
    zu einer messbaren Verbesserung in der Funktion<br>
    hinsichtlich der Beziehung zwischen Nervensystem<br>
    und Bewegungsapparat (Nordahl et al., 2021). Der<br>
    chiropraktische Impuls wirkt auf struktureller Ebene<br>
    (am Gelenk) und im Nervensystem. Der Informations-<br>
    fluss zwischen Körper und Nervensystem wird harmo-<br>
    nisiert und Selbstheilungskräfte aktiviert, um dir eine<br>
    volle Funktionalität und mehr Lebensqualität zu<br>
    ermöglichen.
  </p>
  <svg class="photo" style="left:500px;top:255px" width="251" height="242" viewBox="0 0 251 242" role="img" aria-label="Foto: Chiropraktische Justierung am Rücken einer liegenden Patientin">
    <defs><linearGradient id="gAdjust" x1="0" y1="0" x2="1" y2="1"><stop offset="0" stop-color="#ece7e2"/><stop offset="0.5" stop-color="#c99c80"/><stop offset="1" stop-color="#e8ded6"/></linearGradient></defs>
    <rect width="251" height="5" fill="#b8a67c"/>
    <rect y="5" width="251" height="237" fill="url(#gAdjust)"/>
  </svg>

  <footer class="footer-band">
    <span class="footer-line" style="left:0;width:55px"></span>
    <span style="left:148px">"Time to Connect Your Brain."</span>
    <span style="left:375px">www.chiropraktik-holt.de</span>
    <span style="left:598px">"Time to Connect Your Brain."</span>
    <span class="footer-line" style="left:697px;width:54px"></span>
  </footer>
</section>

</body>
</html>
```